Create a Magazine Ad for an asbestos law firm

we need an 8 X 13 ad to be on the back of a magazine cover. We have the text Attached and want a similar look and feel to our website : www.harborvale-claims.example. The ad should be targeted to white males 55 years or older who are conservative and worked in industry or industrial plants. The main offer is a free case review and trying to get them to call the telephone number.

Target Market(s)

White collar men who worked in industrial plants. Age 55 years or older.

Industry/Entity Type

Legal

Requirements
Must have
• Pictures of white middle class conservative man or man and woman
Nice to have
• look at www.harborvale-claims.example to an. idea of what we are looking for

```html
<!DOCTYPE html>
<html lang="en">
<head>
<meta charset="utf-8">
<title>Mesothelioma Compensation Ad</title>
<link href="https://fonts.googleapis.com/css2?family=Libre+Baskerville:wght@700&family=Open+Sans:ital,wght@0,400;0,600;0,700;0,800;1,400&display=swap" rel="stylesheet">
<style>
:root{
  --navy:#1b2f55;
  --navy-deep:#132442;
  --orange:#e8893a;
  --cream:#fbf4ea;
  --peach:#f3c79a;
  --text:#2b3345;
  --white:#ffffff;
}
*{margin:0;padding:0;box-sizing:border-box}
html,body{width:889px;height:1200px;overflow:hidden;background:#fff}
.ad{position:relative;width:889px;height:1200px;overflow:hidden;font-family:"Open Sans",Arial,sans-serif;color:var(--text);background:var(--white)}
.hero{position:absolute;left:0;top:0;width:889px;height:470px;background:linear-gradient(100deg,var(--cream) 0%,#f8e3cc 45%,var(--peach) 100%)}
.hero-photo{position:absolute;right:0;top:0;width:480px;height:450px;background:radial-gradient(ellipse at 60% 45%,#e9dfd6 0%,#d8c5b3 35%,#f0c08e 75%,rgba(243,199,154,0) 100%)}
.brand{position:absolute;left:56px;top:36px;display:flex;align-items:center;gap:12px}
.brand-dot{width:64px;height:64px;border-radius:50%;background:var(--navy)}
.brand-name{font-weight:700;font-size:17px;color:var(--navy);line-height:1.2;width:120px}
.headline{position:absolute;left:56px;top:150px;width:470px;font-family:"Libre Baskerville",Georgia,serif;font-weight:700;font-size:44px;line-height:1.25;color:var(--navy)}
.wave{position:absolute;left:0;top:400px;width:889px;height:90px}
.body{position:absolute;left:56px;top:492px;width:777px;font-size:15px;line-height:1.5}
.intro{font-style:italic;margin-bottom:4px}
.list{list-style:none;margin-bottom:8px}
.list li{position:relative;padding-left:14px}
.list li::before{content:"";position:absolute;left:0;top:9px;width:6px;height:6px;background:var(--navy)}
.lead{font-weight:700;color:var(--navy)}
.subhead{font-family:"Libre Baskerville",Georgia,serif;font-weight:700;font-size:23px;line-height:1.25;color:var(--navy);margin:10px 0 6px}
.results{position:absolute;left:0;top:935px;width:889px;height:200px}
.results-bg{position:absolute;left:0;top:0;width:889px;height:200px}
.grid{position:absolute;left:90px;top:30px;width:709px;display:grid;grid-template-columns:repeat(3,1fr);gap:14px 22px}
.card{border:2px solid var(--white);height:62px;text-align:center;color:var(--white);padding-top:6px}
.amount{font-weight:800;font-size:20px;line-height:1.2}
.caption{font-size:10px;line-height:1.25;opacity:.9;padding:0 8px}
.footer{position:absolute;left:0;top:1135px;width:889px;height:65px;background:var(--white);display:flex;align-items:center;justify-content:space-between;padding:0 40px}
.footer-text .cta-line{font-weight:700;font-size:16px;color:var(--navy)}
.footer-text .small{font-size:10.5px;line-height:1.35}
.phone-block{text-align:right}
.btn{display:inline-block;background:var(--orange);color:var(--white);font-weight:700;font-size:11px;padding:4px 14px;border-radius:3px}
.phone{font-weight:800;font-size:30px;color:var(--navy);line-height:1.05}
</style>
</head>
<body>
<main class="ad">
  <section class="hero">
    <div class="hero-photo" role="img" aria-label="Photo of a smiling gray-haired older man in a white shirt"></div>
    <div class="brand"><span class="brand-dot"></span><span class="brand-name">Harborvale Claims</span></div>
    <h1 class="headline">Diagnosed with Mesothelioma, You could be Owed Compensation</h1>
  </section>

  <svg class="wave" viewBox="0 0 889 90" preserveAspectRatio="none" aria-hidden="true">
    <path d="M0 40 C220 95 520 0 889 45 L889 90 L0 90 Z" fill="#ffffff"/>
    <path d="M0 40 C220 95 520 0 889 45" fill="none" stroke="#1b2f55" stroke-width="4"/>
    <path d="M0 52 C230 105 530 12 889 57" fill="none" stroke="#e8893a" stroke-width="2"/>
  </svg>

  <section class="body">
    <p class="intro">It's very likely you developed this disease through asbestos exposure. Mesothelioma patients are getting multi-million dollar settlements, decades later, from:</p>
    <ul class="list">
      <li>Exposure to asbestos products,</li>
      <li>Ex-employers, or</li>
      <li>Talcum baby powder companies.</li>
    </ul>
    <p class="lead">We can help you find out if you qualify for a case in minutes.</p>
    <ul class="list">
      <li>We'll analyze your situation at no cost</li>
      <li>Determine how much compensation you could be entitled too</li>
      <li>Show you the next steps to get what you're owed</li>
    </ul>
    <h2 class="subhead">$30 Billion is Available in<br>Trust for Mesothelioma Patients</h2>
    <p>Tradesmen in many industries were negligently exposed to asbestos materials well into the 1980s. Whether you developed Mesothelioma yourself due to asbestos exposure or you're the surviving family of a loved one you could be entitled to significant compensation.</p>
    <h2 class="subhead">How much Money Can People<br>Receive from a Mesothelioma Case?</h2>
    <p>Depending on where you were exposed and a few other factors, you can get a settlement from 6 to 7 figures. Here are a few examples of Mesothelioma Settlements received by our clients. These figures are the total compensation after all attorney fees and expenses are deducted.</p>
  </section>

  <section class="results">
    <svg class="results-bg" viewBox="0 0 889 200" preserveAspectRatio="none" aria-hidden="true">
      <path d="M0 18 C250 -6 600 30 889 6 L889 200 L0 200 Z" fill="#1b2f55"/>
    </svg>
    <div class="grid">
      <div class="card"><div class="amount">$6,742,000</div><div class="caption">Recovered through trusts and legal settlement</div></div>
      <div class="card"><div class="amount">$6,033,000</div><div class="caption">Recovered through trusts and legal settlement</div></div>
      <div class="card"><div class="amount">$5,039,250</div><div class="caption">Recovered through trusts and legal settlement</div></div>
      <div class="card"><div class="amount">$3,901,750</div><div class="caption">Recovered through trusts and legal settlement</div></div>
      <div class="card"><div class="amount">$3,600,440</div><div class="caption">Recovered through trusts and legal settlement</div></div>
      <div class="card"><div class="amount">$2.3 Million</div><div class="caption">Recovered through trusts and legal settlement</div></div>
    </div>
  </section>

  <footer class="footer">
    <div class="footer-text">
      <p class="cta-line">Find out if you're Eligible for FREE, in Minutes.</p>
      <p class="small">We'll evaluate your situation and tell you what your case could be worth.<br>Marlow &amp; Keane, LLP, Daniel Marlow, Houston, TX</p>
    </div>
    <div class="phone-block">
      <span class="btn">GET YOUR FREE EVALUATION NOW!</span>
      <p class="phone">CALL 1-555 0142</p>
    </div>
  </footer>
</main>
</body>
</html>
```